Product Launch HTML Email Design

Plinth Quarry. Email blast for quickest and easiest property research tool. quickest and easiest way to find property ownership records including names, phone numbers, and mailing addresses. brokers spend less time collecting information and more time prospecting.
Updates
Also, it has to be run by a spam checker. Thank you I have posted under the new file, a skyline picture that HAS to be use. The old skyline can''t be used. I apologize for any inconvenience this may have caused. Please remember that it has to be HTML design. If it''s not, the flyer won''t be visible to recepients that don''t have allow images on their emails.
Target Market(s)
Males, ages 20-55, income 100k/yr+, commercial real estate brokers
Industry/Entity Type
Product
Requirements
Must have
- Logo. Design must be consistent with http://www.plinthquarry-example.com/blogger which will be used as the landing page for the email blast as well. Email is encouraged to link to this page. $50/month for unlimited property records.
Nice to have
- suggested subject lines
Should not have
- Should not look cluttered. Message should not be in a big image only in case the viewer does not select to view images. Should not look cluttered.

```html
<!DOCTYPE html>
<html lang="en">
<head>
<meta charset="utf-8">
<title>Plinth Quarry – Just One Email!</title>
<link rel="stylesheet" href="https://fonts.googleapis.com/css2?family=Archivo+Black&family=Arimo:ital,wght@0,400;0,700;1,400;1,700&display=swap">
<style>
  :root {
    --green: #4ee000;
    --green-deep: #2fb000;
    --green-pale: #d6ff9a;
    --ink: #3c3c3c;
    --ink-soft: #555555;
    --paper: #ffffff;
    --pattern: #eeeeee;
    --city-dark: #6f7378;
    --city-light: #dfe2e5;
  }
  * { margin: 0; padding: 0; box-sizing: border-box; }
  html, body { width: 847px; height: 1200px; overflow: hidden; background: var(--paper); }
  .flyer {
    position: relative; width: 847px; height: 1200px; overflow: hidden;
    background: var(--paper);
    font-family: "Arimo", Arial, sans-serif; color: var(--ink);
  }
  .top-band {
    position: absolute; left: 0; top: 0; width: 100%; height: 72px;
    background: linear-gradient(180deg, var(--green) 0%, #9bf23d 55%, rgba(255,255,255,0) 100%);
  }
  .backdrop-pattern {
    position: absolute; left: 0; top: 60px; width: 100%; height: 940px;
    background: linear-gradient(160deg, var(--paper) 0%, var(--pattern) 45%, var(--paper) 100%);
    opacity: .8;
  }
  .brand {
    position: absolute; left: 40px; top: 44px;
    display: flex; align-items: center; gap: 16px;
  }
  .brand-dot { width: 74px; height: 74px; border-radius: 50%; background: var(--green); }
  .brand-name { font-size: 34px; font-weight: 700; color: var(--green-deep); line-height: 1; }
  .brand-tagline { font-size: 15px; color: var(--ink-soft); margin-top: 6px; }
  .content { position: absolute; left: 0; top: 0; width: 100%; text-align: center; }
  .headline {
    position: absolute; left: 0; top: 232px; width: 100%;
    font-family: "Archivo Black", "Arial Black", sans-serif;
    font-size: 84px; letter-spacing: 1px; color: var(--green);
    text-shadow: 0 0 2px var(--green-deep);
  }
  .intro {
    position: absolute; left: 60px; top: 360px; width: 727px;
    font-size: 31px; line-height: 38px; color: var(--ink);
  }
  .intro .product { font-style: italic; font-size: 40px; color: var(--green); }
  .features {
    position: absolute; left: 0; top: 482px; width: 100%; list-style: none;
    font-style: italic; font-weight: 700; font-size: 34px; line-height: 48px;
    color: var(--green);
  }
  .benefit {
    position: absolute; left: 40px; top: 740px; width: 767px;
    font-weight: 700; font-size: 29px; line-height: 40px; color: var(--ink-soft);
  }
  .skyline {
    position: absolute; left: 0; bottom: 0; width: 100%; height: 240px;
    background: linear-gradient(180deg, var(--city-light) 0%, #a8adb2 45%, var(--city-dark) 100%);
  }
  .price {
    position: absolute; right: 77px; top: 910px; text-align: right;
    font-weight: 700; font-size: 29px; line-height: 36px; color: var(--ink);
  }
  .price .only {
    font-family: "Archivo Black", "Arial Black", sans-serif;
    font-size: 34px; color: var(--green);
  }
</style>
</head>
<body>
<main class="flyer">
  <div class="backdrop-pattern" role="img" aria-label="Faint background of rotated property names, addresses and phone numbers"></div>
  <div class="top-band"></div>

  <header class="brand">
    <span class="brand-dot"></span>
    <div>
      <div class="brand-name">Plinth Quarry</div>
      <div class="brand-tagline">Let Brokers be Brokers</div>
    </div>
  </header>

  <section class="content">
    <h1 class="headline">JUST ONE EMAIL!</h1>
    <p class="intro"><span class="product">Plinth Quarry</span> is the quickest and easiest way to find property ownership records including:</p>
    <ul class="features">
      <li>Names</li>
      <li>Phone numbers</li>
      <li>Mailing addresses</li>
    </ul>
    <p class="benefit">Brokers spend less time collecting information and more time prospecting.</p>
  </section>

  <div class="skyline" role="img" aria-label="City skyline of office towers in grey tones"></div>

  <p class="price"><span class="only">ONLY</span> $50/month<br>for unlimited property<br>records</p>
</main>
</body>
</html>
```